Web Developer Needs a Business Card Design

I need a personal business card design that represents me as a web developer for potential employers. I would like the background to be a dark color on the front for contrast with my logo and name. The back will have all my information along with a smaller version of the logo. I want something with a modern look and feel, not too conservative. This will be used for potential employers and freelance work.

Industry/Entity Type

Business

Contact Information for Business Card

Front should have my logo and name. The back should have all my personal information which would include: name: Tom Brevardi, phone: 570-614-9083, email: tombrevardi@mailwisp.com, website url: www.tombrevardi.com, logo, web developer.

Font styles to use
Sans Serif

Requirements
Must have
• Must include my logo. The color palette base color will be the logo color.

```html
<!DOCTYPE html>
<html lang="en">
<head>
<meta charset="utf-8">
<title>Tom Brevardi – Business Card</title>
<link href="https://fonts.googleapis.com/css2?family=Open+Sans:wght@400;600;700&display=swap" rel="stylesheet">
<style>
  :root {
    --teal: #5cc2ab;
    --ink: #0c0c0c;
    --paper: #ffffff;
    --stage: #e9e7e3;
    --text-light: #f2f2f2;
  }
  * { margin: 0; padding: 0; box-sizing: border-box; }
  html, body { width: 1200px; height: 913px; overflow: hidden; }
  body {
    background: var(--stage);
    font-family: "Open Sans", Arial, sans-serif;
    position: relative;
  }
  .card {
    position: absolute;
    top: 306px;
    width: 525px;
    height: 300px;
    border-radius: 18px;
    overflow: hidden;
    background: var(--ink);
    box-shadow: 0 10px 30px rgba(0,0,0,0.25);
  }
  .card--info { left: 50px; }
  .card--front { left: 625px; }

  .info-shape { position: absolute; inset: 0; }

  .info-mark {
    position: absolute;
    left: 30px;
    top: 60px;
    width: 190px;
    text-align center;
    text-align: center;
  }
  .info-mark .ring {
    width: 136px; height: 136px;
    margin: 0 auto 12px;
    border: 13px solid var(--teal);
    border-radius: 50%;
  }
  .info-mark .wordmark {
    color: var(--teal);
    font-weight: 700;
    font-size: 17px;
    letter-spacing: 0.5px;
  }

  .contact {
    position: absolute;
    right: 28px;
    top: 36px;
    text-align: right;
    color: var(--text-light);
  }
  .contact .name {
    font-weight: 700;
    font-size: 20px;
    letter-spacing: 1px;
    text-transform: uppercase;
    line-height: 1.1;
  }
  .contact .role {
    color: var(--teal);
    font-weight: 700;
    font-size: 12px;
    letter-spacing: 1px;
    text-transform: uppercase;
    margin-bottom: 14px;
  }
  .contact .line {
    font-size: 13px;
    line-height: 21px;
    display: flex;
    justify-content: flex-end;
    align-items: center;
    gap: 7px;
  }
  .contact .line svg { width: 12px; height: 12px; flex: none; }

  .front-mark {
    position: absolute;
    left: 50%;
    top: 56px;
    width: 104px; height: 104px;
    margin-left: -52px;
    border: 10px solid var(--teal);
    border-radius: 50%;
  }
  .front-name {
    position: absolute;
    top: 182px;
    width: 100%;
    text-align: center;
    color: var(--text-light);
    font-size: 32px;
    font-weight: 400;
    letter-spacing: 3px;
    text-transform: uppercase;
  }
  .front-role {
    position: absolute;
    top: 228px;
    width: 100%;
    text-align: center;
    color: var(--text-light);
    font-size: 17px;
    letter-spacing: 0.5px;
  }
</style>
</head>
<body>

  <section class="card card--info" aria-label="Card back with contact details">
    <svg class="info-shape" viewBox="0 0 525 300" width="525" height="300" aria-hidden="true">
      <path d="M0 0 H214 C294 70 304 230 236 300 H0 Z" fill="var(--teal)"/>
      <path d="M0 0 H206 C286 70 296 230 228 300 H0 Z" fill="var(--ink)"/>
      <path d="M0 0 H202 C281 70 291 230 224 300 H0 Z" fill="var(--paper)"/>
    </svg>

    <div class="info-mark">
      <div class="ring"></div>
      <div class="wordmark">Tom Brevardi</div>
    </div>

    <div class="contact">
      <div class="name">Tom Brevardi</div>
      <div class="role">Web Developer</div>
      <div class="line">570-614-9083
        <svg viewBox="0 0 24 24" aria-hidden="true"><path fill="var(--teal)" d="M6.6 10.8a15.1 15.1 0 0 0 6.6 6.6l2.2-2.2c.3-.3.7-.4 1-.2 1.1.4 2.3.6 3.6.6.6 0 1 .4 1 1V20c0 .6-.4 1-1 1A17 17 0 0 1 3 4c0-.6.4-1 1-1h3.5c.6 0 1 .4 1 1 0 1.3.2 2.5.6 3.6.1.3 0 .7-.2 1z"/></svg>
      </div>
      <div class="line">tombrevardi@mailwisp.com
        <svg viewBox="0 0 24 24" aria-hidden="true"><rect x="2.5" y="5" width="19" height="14" rx="1.5" fill="none" stroke="var(--teal)" stroke-width="2.2"/><path d="M3 6l9 7 9-7" fill="none" stroke="var(--teal)" stroke-width="2.2"/></svg>
      </div>
      <div class="line">www.tombrevardi.com
        <svg viewBox="0 0 24 24" aria-hidden="true"><circle cx="12" cy="12" r="9.5" fill="none" stroke="var(--teal)" stroke-width="2"/><ellipse cx="12" cy="12" rx="4" ry="9.5" fill="none" stroke="var(--teal)" stroke-width="2"/><path d="M2.5 12h19" stroke="var(--teal)" stroke-width="2"/></svg>
      </div>
    </div>
  </section>

  <section class="card card--front" aria-label="Card front">
    <div class="front-mark"></div>
    <div class="front-name">Tom Brevardi</div>
    <div class="front-role">Front-End Developer</div>
  </section>

</body>
</html>
```